Dietitian needs awesome business card

I need a contemporary design that's eye catching but professional.
My card is to given to doctors, specialists and patients alike.
I manage patients with chronic diseases
I have uploaded my logo and current business card, I would also like the other Registered Clinical Nutritionist logo incorporated into the design

Target Market(s)

Doctors, specialists and patients

Industry/Entity Type

Healthcare

Contact Information for Business Card

www.brindlecovenutrition.com.au
Ph: 0427 516 903
Fax: 6482 7315
email: marcus.k.wellfare@quorvamail.com
Space on the back of the card with: Appointment date, Appointment time and appointment location

Font styles to use
Serif

Colors
fbee3e
876aae
ffc214

Requirements
Must have
• My Logo
• Registered Clinical Nutritionist Logo
• My 4 locations - Fernhollow Medical Centre, North Kelby Health, Ashcourt Medical, Pinebrook Doctors Surgery
Nice to have
• I like the colours in my current business card

```html
<!DOCTYPE html>
<html lang="en">
<head>
<meta charset="utf-8">
<title>Brindlecove Nutrition &amp; Dietetics – Business Card</title>
<link href="https://fonts.googleapis.com/css2?family=Libre+Franklin:wght@400;600;700&display=swap" rel="stylesheet">
<style>
  :root{
    --backdrop:#4a3f3a;
    --card:#1c1c1e;
    --line:#8d8d92;
    --ink:#ececec;
    --blue:#2f56c4;
    --green:#8cc63f;
    --orange:#f26b21;
  }
  *{box-sizing:border-box;margin:0;padding:0}
  html,body{width:1200px;height:787px;overflow:hidden}
  body{background:var(--backdrop);font-family:"Libre Franklin",Arial,sans-serif;position:relative}
  .card{position:absolute;width:560px;height:330px;background:var(--card);border-radius:3px;box-shadow:0 6px 18px rgba(0,0,0,.35)}
  .card--back{left:40px;top:50px}
  .card--front{left:600px;top:405px}

  /* back */
  .back-mark{position:absolute;left:28px;top:22px;display:flex;align-items:center;gap:8px;color:var(--green);font-weight:700;font-size:13px}
  .mark-dot{width:14px;height:14px;border-radius:50%;background:var(--green)}
  .rule{position:absolute;height:1px;background:var(--line)}
  .field-label{position:absolute;color:var(--blue);font-size:14px;font-style:normal}
  .badge{position:absolute;right:28px;top:26px;width:120px;height:70px;background:var(--orange)}
  .locations{position:absolute;list-style:none;color:var(--ink);font-size:12px;line-height:22px}
  .locations li{display:flex;align-items:center;gap:7px}
  .box{width:10px;height:10px;border:1px solid var(--ink)}
  .ampm{position:absolute;right:36px;top:212px;color:var(--blue);font-size:11px}

  /* front */
  .brand{position:absolute;left:230px;top:70px;display:flex;align-items:center;gap:12px}
  .brand-dot{width:44px;height:44px;border-radius:50%;background:var(--green)}
  .brand-name{color:var(--blue);font-weight:700;font-size:22px;line-height:1.15}
  .person{position:absolute;left:36px;top:170px;width:270px;text-align:right}
  .person-name{color:var(--blue);font-weight:700;font-size:19px}
  .person-role{color:var(--green);font-weight:700;font-size:14px;margin-top:4px}
  .person-email{color:var(--ink);font-size:12.5px;margin-top:8px}
  .divider{position:absolute;left:322px;top:172px;width:1px;height:96px;background:var(--line)}
  .contacts{position:absolute;left:338px;top:178px;list-style:none;color:var(--ink);font-size:14px}
  .contacts li{display:flex;align-items:center;gap:9px;height:27px}
  .contacts svg{width:16px;height:16px;fill:var(--blue)}
  .contacts .web{font-size:12.5px}
</style>
</head>
<body>

<section class="card card--back" aria-label="Appointment side">
  <div class="back-mark"><span class="mark-dot"></span>Brindlecove</div>
  <div class="badge" role="img" aria-label="Registered Clinical Nutritionist badge"></div>

  <div class="rule" style="left:28px;top:70px;width:380px"></div>
  <div class="rule" style="left:28px;top:100px;width:380px"></div>
  <span class="field-label" style="left:28px;top:124px">Date :</span>
  <div class="rule" style="left:78px;top:140px;width:454px"></div>
  <span class="field-label" style="left:290px;top:196px">Time :</span>
  <div class="rule" style="left:340px;top:212px;width:140px"></div>
  <span class="ampm">AM/PM</span>

  <ul class="locations" style="left:28px;top:170px">
    <li><span class="box"></span>Fernhollow Medical Centre</li>
    <li><span class="box"></span>North Kelby Health</li>
  </ul>
  <ul class="locations" style="left:290px;top:236px">
    <li><span class="box"></span>Pinebrook Doctors Surgery</li>
    <li><span class="box"></span>Ashcourt Medical</li>
  </ul>
</section>

<section class="card card--front" aria-label="Contact side">
  <div class="brand">
    <span class="brand-dot"></span>
    <span class="brand-name">Brindlecove<br>Nutrition &amp; Dietetics</span>
  </div>

  <div class="person">
    <p class="person-name">Marcus Kellaway</p>
    <p class="person-role">Nutritionist &amp; Chef</p>
    <p class="person-email">marcus.k.wellfare@quorvamail.com</p>
  </div>

  <div class="divider"></div>

  <ul class="contacts">
    <li><svg viewBox="0 0 24 24"><path d="M6.6 10.8a15.1 15.1 0 0 0 6.6 6.6l2.2-2.2a1 1 0 0 1 1-.25 11.4 11.4 0 0 0 3.6.57 1 1 0 0 1 1 1V20a1 1 0 0 1-1 1A17 17 0 0 1 3 4a1 1 0 0 1 1-1h3.5a1 1 0 0 1 1 1c0 1.25.2 2.45.57 3.57a1 1 0 0 1-.25 1z"/></svg>0427 516 903</li>
    <li><svg viewBox="0 0 24 24"><path d="M7 3h10v5H7zM4 9h16a2 2 0 0 1 2 2v6h-4v4H6v-4H2v-6a2 2 0 0 1 2-2zm4 7v3h8v-3z"/></svg>6482 7315</li>
    <li class="web"><svg viewBox="0 0 24 24"><path d="M12 2a10 10 0 1 0 0 20 10 10 0 0 0 0-20zm6.9 6h-2.9a15 15 0 0 0-1.4-3.6A8 8 0 0 1 18.9 8zM12 4c.8 1.2 1.5 2.5 1.9 4h-3.8c.4-1.5 1.1-2.8 1.9-4zM4.3 14a8 8 0 0 1 0-4h3.3a16 16 0 0 0 0 4zm.8 2h2.9a15 15 0 0 0 1.4 3.6A8 8 0 0 1 5.1 16zM8 8H5.1a8 8 0 0 1 4.3-3.6A15 15 0 0 0 8 8zm4 12c-.8-1.2-1.5-2.5-1.9-4h3.8c-.4 1.5-1.1 2.8-1.9 4zm2.3-6H9.7a14 14 0 0 1 0-4h4.6a14 14 0 0 1 0 4zm.3 5.6A15 15 0 0 0 16 16h2.9a8 8 0 0 1-4.3 3.6zM16.4 14a16 16 0 0 0 0-4h3.3a8 8 0 0 1 0 4z"/></svg>www.brindlecovenutrition.com.au</li>
  </ul>
</section>

</body>
</html>
```